Design a DL flyer double sided 4 colour 210mm x 95 mm (portrait) for the launch of a new yoga studio opening in North Melbourne on the 23 November 2013.
The final design should communicate with a strong call to action- the opening date , register to receive your first class free and like us on FriendPage.
The studio provides a tranquil, open space to practice yoga, create a feeling of light, peace and a nurturing environment, please create this feeling in the design.

An example design mock (rough design feel free to move around as required, includes final content) print specifications, logo, typography style and image attached.
The reverse side to include logo, address and please design the timetable for the launch week (refer design mock)
Have also attached a reverse logo for a dark background and are open to designer providing examples with various background colours and effects.
Back content can be moved to the front side if required to facilitate design

Target Market(s)

People in the area who are practicing yoga elsewhere and encourage them to come to the studio to try us out with a free opening offer in our first week. And people new to yoga wanting to give it a try.
Experienced yoga people and people new to yoga - all ages

Industry/Entity Type

Environment

Requirements
Must have
• The Calm Haven logo physical address, website address, the tagline live, breathe, love...
The final design should communicate with a strong call to action- the opening date , register to receive your first class free and like us on FriendPage. and the website address thecalmhaven.com.au, drive them to the website to register.
The studio provides a tranquil, open space to practice yoga, create a feeling of light, peace and a nurturing environment, please create this feeling in the design

```html
<!DOCTYPE html>
<html lang="en">
<head>
<meta charset="utf-8">
<title>The Calm Haven – New Studio Opening Flyer</title>
<link href="https://fonts.googleapis.com/css2?family=Arimo:ital,wght@0,400;0,700;1,400&family=Roboto+Condensed:wght@700&display=swap" rel="stylesheet">
<style>
  :root{
    --orange-top:#f9a51f;
    --orange-bottom:#f07224;
    --ink:#111111;
    --white:#ffffff;
    --grey:#9a9a9a;
    --rule:rgba(255,255,255,.55);
    --map-tone:#fbe3c6;
  }
  *{box-sizing:border-box;margin:0;padding:0}
  html,body{width:1200px;height:1000px;overflow:hidden;background:var(--white)}
  body{position:relative;font-family:"Arimo",Arial,sans-serif;color:var(--ink)}

  .flyer-side{position:absolute;top:0;width:452px;height:1000px}
  .front{left:115px;background:linear-gradient(180deg,var(--orange-top) 0%,var(--orange-bottom) 100%)}
  .back{left:628px}

  /* front */
  .brand-bar{position:absolute;top:0;left:0;width:100%;height:163px;background:var(--ink)}
  .brand-name{position:absolute;left:40px;top:56px;display:flex;align-items:center;gap:12px;
    font-weight:700;font-size:34px;color:var(--white)}
  .brand-dot{width:34px;height:34px;border-radius:50%;background:var(--orange-top)}
  .tagline{position:absolute;left:38px;top:124px;font-style:italic;font-size:17px;color:var(--white)}

  .headline-block{position:absolute;left:0;width:100%;text-align:center;font-family:"Roboto Condensed","Arial Narrow",sans-serif;font-weight:700}
  .star{font-size:56px;line-height:1;height:34px;display:block}
  .opening{top:308px}
  .opening .big{font-size:74px;line-height:70px;letter-spacing:-1px}
  .opening .mid{font-size:48px;line-height:46px}
  .underline{display:block;width:380px;height:2px;background:var(--ink);margin:4px auto 0}
  .opening-date{position:absolute;top:490px;width:100%;text-align:center}
  .opening-date .date{font-family:"Roboto Condensed","Arial Narrow",sans-serif;font-weight:700;font-size:29px;line-height:32px}
  .opening-date .address{font-size:20px;line-height:26px}
  .offer{top:646px}
  .offer .mid{font-size:45px;line-height:48px;letter-spacing:-.5px}
  .offer-note{position:absolute;top:744px;width:100%;text-align:center;font-size:19px}
  .cta{position:absolute;top:928px;width:100%;text-align:center;font-size:19px;line-height:23px}

  /* back */
  .about{position:absolute;top:0;left:0;width:100%;height:705px;background:linear-gradient(180deg,var(--orange-top) 0%,var(--orange-bottom) 100%)}
  .about-copy{position:absolute;top:42px;left:56px;width:340px;text-align:center;font-size:18.5px;line-height:27px}
  .about-copy em{font-style:italic}
  .timetable-title{position:absolute;top:496px;width:100%;text-align:center;font-family:"Roboto Condensed","Arial Narrow",sans-serif;font-weight:700;font-size:19px}
  .timetable{position:absolute;top:534px;left:28px;width:395px;border-collapse:collapse;color:var(--white);table-layout:fixed}
  .timetable th{background:var(--ink);font-weight:400;font-size:17px;height:25px;border-left:1px solid var(--rule)}
  .timetable td{font-size:11px;height:22.5px;text-align:center;border-left:1px solid var(--rule);border-top:1px solid var(--rule)}
  .timetable th:first-child,.timetable td:first-child{border-left:none}

  .contact{position:absolute;top:705px;left:0;width:100%;height:295px;background:var(--white);text-align:center}
  .contact-brand{display:inline-flex;align-items:center;gap:7px;margin-top:32px;font-weight:700;font-size:17px;color:var(--orange-bottom)}
  .contact-brand .brand-dot{width:18px;height:18px;background:var(--orange-top)}
  .contact-list{list-style:none;margin-top:14px;font-size:13px;line-height:20px;color:#333}
  .contact-list .label{color:var(--grey)}
  .map{position:absolute;left:0;top:132px;width:100%;height:163px;background:linear-gradient(180deg,var(--white) 0%,var(--map-tone) 100%)}
</style>
</head>
<body>

<section class="flyer-side front">
  <header class="brand-bar">
    <div class="brand-name"><span class="brand-dot"></span>The Calm Haven</div>
    <p class="tagline">“live, breathe, love…”</p>
  </header>

  <div class="headline-block opening">
    <span class="star">*</span>
    <div class="big">NEW YOGA</div>
    <div class="mid">STUDIO OPENING</div>
    <span class="underline"></span>
  </div>
  <div class="opening-date">
    <div class="date">23 NOVEMBER</div>
    <div class="address">47 Harbour Lane, North Melbourne</div>
  </div>

  <div class="headline-block offer">
    <span class="star">*</span>
    <div class="mid">FIRST CLASS FREE</div>
    <span class="underline"></span>
  </div>
  <p class="offer-note">in opening week 23 Nov – 29 Nov inclusive</p>

  <p class="cta">To book your free class go online to<br>register and book, like us on FriendPage</p>
</section>

<section class="flyer-side back">
  <div class="about">
    <p class="about-copy">
      A generously sized dedicated yoga studio in North Melbourne, providing dynamic flow vinyasa and restorative yoga for all levels from newbies to ex-perienced, with a collection of the best teachers.<br>
      Embark on a journey to happiness within yourself – be healthy in your body and mind.<br>
      Science is finally proving what yogis have known all along.... <em>yoga is good for you!</em><br>
      A tranquil space to de stress, build strength and healing in our bodies through our own tapas (internal heat).
    </p>

    <h2 class="timetable-title">CLASS TIMES</h2>
    <table class="timetable">
      <thead>
        <tr><th>sat</th><th>sun</th><th>mon</th><th>tue</th><th>wed</th><th>thu</th><th>fri</th></tr>
      </thead>
      <tbody>
        <tr><td>9.00 am</td><td>9.00 am</td><td>6.30 am</td><td>6.30 am</td><td>6.30 am</td><td>6.30 am</td><td>6.30 am</td></tr>
        <tr><td>10.30 am</td><td>10.30 am</td><td>9.30 am</td><td>9.30 am</td><td>9.30 am</td><td>9.30 am</td><td>9.30 am</td></tr>
        <tr><td>4.00 pm</td><td>4.00 pm</td><td>12.30 pm</td><td>12.30 pm</td><td>12.30 pm</td><td>12.30 pm</td><td>12.30 am</td></tr>
        <tr><td></td><td></td><td>5.30 pm</td><td>5.30 pm</td><td>5.30 pm</td><td>5.30 pm</td><td>5.30 pm</td></tr>
        <tr><td></td><td></td><td>7.00pm</td><td>7.00pm</td><td>7.00pm</td><td>7.00pm</td><td>7.00pm</td></tr>
      </tbody>
    </table>
  </div>

  <div class="contact">
    <div class="contact-brand"><span class="brand-dot"></span>The Calm Haven</div>
    <ul class="contact-list">
      <li><span class="label">website</span> thecalmhaven.com.au</li>
      <li><span class="label">social</span> The Calm Haven - Melbourne</li>
      <li><span class="label">telephone</span> 0491-555210</li>
    </ul>
    <div class="map" role="img" aria-label="Street map showing the studio location in North Melbourne with nearby streets and landmarks"></div>
  </div>
</section>

</body>
</html>
```